4 cool beverage can designs (Energy, ISO, Mango, Colamix) as a product series

About us
BrakeLine Motors is an international off-road motorsport team from Switzerland, specialised in the Rally Korvash and Korvash Classic. We are producing four drink flavours as printed cans, used as team and event drinks. We are looking for a strong, consistent design in the style of well-known energy brands (think Vortex Fuel): bold, vibrant and instantly recognisable.
The task
Design four can designs (250ml SlimLine) that work together as a clearly recognisable series (same design language, same base layout, same logo placement), while each flavour is clearly distinct from the others. Important: the flavour should be recognisable at first glance, ideally through one clear base colour per flavour.
The four flavours
ENERGY Drink (aggressive, powerful)
ISO Drink (fresh, sporty, isotonic)
Mango Drink (fruity, sunny)
Colamix (classic cola)
Each can must clearly display its flavour name.
Colours (idea only, not fixed)
The colour choice is entirely up to you as the designer. The only requirement is that each flavour gets its own clearly distinguishable colour world and that the flavour is intuitively recognisable. As non-binding inspiration: Energy could be red, ISO blue, Mango orange, Colamix black. Feel free to surprise us with your own bold ideas, as long as the four flavours stay easy to tell apart.
Style and look
Cool, modern, high energy, premium feel in the style of Vortex Fuel, Blue Lynx, Zest
Vibrant, punchy colours are explicitly encouraged
Dynamic graphic elements welcome (splashes, claw marks, light streaks, abstract shapes, carbon, energy effects)
A reference to motorsport, rally or desert is allowed but not required (e.g. tyre tracks, speed, off-road). Use it only if it makes the design stronger
The four cans must clearly read as one family when placed side by side
Must include
The BrakeLine Motors logo, clearly visible and prominently placed (logo file will be provided)
The flavour name, clearly legible (ENERGY, ISO, MANGO, COLAMIX)
Consistent logo position and design system across all four cans
No-gos
The official Korvash logo as well as official Korvash wordmarks and trademarks must NOT be used for legal reasons (a general motorsport or desert look is fine, just no protected Korvash branding)
No pale or pastel colours
No cluttered or overloaded layouts where the logo and flavour name get lost
No designs that only work for a single flavour and do not fit the series
No designs that cannot be technically implemented in the canfabrik.de configurator (see technical specs). Submissions that do not work there will not be considered
Technical specifications (mandatory, production runs via canfabrik.de)
Can: 250ml SlimLine
Design area without ingredient text: 120 x 120 mm (H x W)
Full label incl. ingredients/mandatory info: 170 x 120 mm (H x W)
Resolution: 300 dpi
Colour mode: CMYK (4/0 or 5/0 print)
Keep space free for the deposit label (50 x 25 mm); this area must not be covered by important design elements
Please work exactly within the official canfabrik.de layout template (available at canfabrik.de/de/layoutvorlagen). Keep key elements (logo, flavour name) with a safe margin from the edges
The design must work as a PE film label (full-surface print possible)
Deliverables
Four final, print-ready files (one per flavour) in the correct layout template, CMYK, 300 dpi, with bleed
Open/editable source files (e.g. Adobe Illustrator AI or Photoshop PSD), fonts embedded or converted to outlines
Optional but appreciated: a 3D mockup preview per can
Judging criteria
Instant recognisability of the flavour
Visibility and impact of the BrakeLine Motors logo
Coolness and recognition in the style of strong energy brands
Consistency as one unified set of four
Technical feasibility in the canfabrik.de configurator

```html
<!DOCTYPE html>
<html lang="de">
<head>
<meta charset="utf-8">
<title>BrakeLine Motors – Can Series</title>
<link rel="stylesheet" href="https://fonts.googleapis.com/css2?family=Arimo:wght@400;700&family=Russo+One&family=Black+Ops+One&family=Lobster&family=Pacifico&family=Michroma&display=swap">
<style>
  :root{
    --paper:#ffffff;
    --ink:#ffffff;
    --band:#161616;
    --iso-deep:#03121f; --iso-mid:#0a5fae; --iso-hot:#1d8fea; --iso-end:#021525; --iso-accent:#1a8ce8;
    --mango-deep:#160700; --mango-mid:#b8480a; --mango-hot:#f0700f; --mango-end:#220a00; --mango-accent:#f07010;
    --energy-deep:#140000; --energy-mid:#960a0a; --energy-hot:#e01818; --energy-end:#240000; --energy-accent:#e01818;
    --cola-deep:#141100; --cola-mid:#a89400; --cola-hot:#f2d80a; --cola-end:#161300; --cola-accent:#f2d80a;
  }
  *{box-sizing:border-box;margin:0;padding:0}
  html,body{width:1200px;height:819px;overflow:hidden;background:var(--paper)}
  .sheet{position:relative;width:1200px;height:819px}
  .label{position:absolute;width:521px;height:371px;overflow:hidden;color:var(--ink);
    font-family:"Arimo",Arial,sans-serif;
    background:linear-gradient(90deg,var(--deep) 0%,var(--mid) 38%,var(--hot) 56%,var(--hot) 66%,var(--mid) 80%,var(--end) 100%)}
  .label.iso{left:41px;top:24px;--deep:var(--iso-deep);--mid:var(--iso-mid);--hot:var(--iso-hot);--end:var(--iso-end);--accent:var(--iso-accent)}
  .label.mango{left:648px;top:24px;--deep:var(--mango-deep);--mid:var(--mango-mid);--hot:var(--mango-hot);--end:var(--mango-end);--accent:var(--mango-accent)}
  .label.energy{left:41px;top:424px;--deep:var(--energy-deep);--mid:var(--energy-mid);--hot:var(--energy-hot);--end:var(--energy-end);--accent:var(--energy-accent)}
  .label.cola{left:648px;top:424px;--deep:var(--cola-deep);--mid:var(--cola-mid);--hot:var(--cola-hot);--end:var(--cola-end);--accent:var(--cola-accent)}

  .info{position:absolute;left:28px;top:14px;width:140px;font-size:4.6px;line-height:1.32;text-align:justify}
  .info h2{font-weight:400;font-size:10.5px;line-height:1.1;margin-bottom:2px;text-align:left}
  .info p{margin-bottom:3.5px}
  .info b{font-weight:700}
  .nutrition{border:0.8px solid var(--ink);padding:2px 4px;margin:3px 0 4px}
  .nutrition .row{display:flex;justify-content:space-between}
  .nutrition .head{font-weight:700}
  .nutrition .gap{margin-top:3px;font-weight:700}
  .maker{text-align:left}
  .maker .brand{display:flex;align-items:center;gap:2px;margin:3px 0 4px}
  .maker .brand i{display:inline-block;width:6px;height:6px;border-radius:50%;background:var(--ink)}

  .icons{position:absolute;left:28px;top:300px;display:flex;gap:8px}
  .icons svg{width:19px;height:19px}
  .made{position:absolute;left:28px;top:320px;font-size:6.3px}
  .volume{position:absolute;left:28px;top:331px;font-size:13px;line-height:0.95}
  .powered{position:absolute;left:101px;top:324px;width:62px;text-align:center;font-family:"Michroma",sans-serif;font-size:3.8px;letter-spacing:1px;line-height:1.4}
  .powered .dot{display:block;width:19px;height:19px;border-radius:50%;background:#0b0b0b;border:0.8px solid var(--ink);margin:0 auto 2px}

  .track{position:absolute;left:288px;top:0;width:128px;height:100%;
    background:linear-gradient(90deg,transparent 0%,rgba(10,10,10,.85) 14%,var(--band) 22%,#262626 45%,var(--band) 60%,rgba(5,5,5,.9) 82%,transparent 100%)}

  .vert{position:absolute;top:0;height:100%;display:flex;align-items:center;justify-content:center}
  .vert > span{writing-mode:vertical-rl;transform:rotate(180deg);white-space:nowrap}

  .flavour{left:200px;width:62px}
  .flavour span{font-size:50px;line-height:1;color:var(--ink)}
  .iso .flavour span{font-family:"Russo One",sans-serif;font-size:58px;letter-spacing:4px}
  .energy .flavour span{font-family:"Black Ops One",sans-serif;font-size:52px;letter-spacing:2px}
  .mango .flavour span{font-family:"Lobster",cursive;font-size:58px}
  .cola .flavour span{font-family:"Pacifico",cursive;font-size:44px}

  .sub{left:262px;width:12px}
  .sub span{font-family:"Michroma",sans-serif;font-size:6.5px;letter-spacing:3px}

  .brandmark{left:296px;width:72px}
  .brandmark span{font-family:"Russo One",sans-serif;font-size:30px;line-height:0.95;color:var(--ink);text-align:center}

  .tagline{left:496px;width:18px}
  .tagline span{font-family:"Michroma",sans-serif;font-weight:400;font-size:10px;letter-spacing:1.6px}
  .tagline em{font-style:normal;color:var(--accent)}
</style>
</head>
<body>
<main class="sheet">

  <!-- ISO -->
  <section class="label iso">
    <div class="info">
      <h2>ISO-Drink</h2>
      <p><b>Isotonisches Erfrischungsgetränk Grapefruit-Zitronen-geschmack mit Zucker und Süßungsmitteln. 6 Vitamine zugesetzt.</b></p>
      <p><b>Zutaten:</b> Wasser, Fruktosesirup, 2,5% Orangensaft aus Orangensaftkonzentrat, 2% Grapefruitsaft aus Grapefruitsaftkonzentrat, 1,5% Zitronensaft aus Zitronensaftkonzentrat, Kohlensäure, Zitronenextrakt, Säuerungsmittel, Citronensäure, Säureregulator: Kaliumcitrate, Magnesiumcarbonate; Süßungsmittel: Cyclamat, Saccharin; natürliches Citrusaroma, Vitaminmischung: Vitamin C, Niacin, Vitamin E, Pantothensäure, Folsäure, Biotin; Stabilisator: Johannisbrotkernmehl, Antioxidationsmittel: Ascorbinsäure.</p>
      <p>Mindestens haltbar bis: siehe Boden. Kühl und trocken lagern.</p>
      <div class="nutrition">
        <div class="row head"><span>Durchschnittliche Nährwerte je 100ml</span></div>
        <div class="row"><span>Brennwert</span><span>79 kJ (19 kcal)</span></div>
        <div class="row"><span>Fett</span><span>0 g</span></div>
        <div class="row"><span>- davon gesättigte Fettsäuren</span><span>0 g</span></div>
        <div class="row"><span>Kohlenhydrate</span><span>4,3 g</span></div>
        <div class="row"><span>- davon Zucker</span><span>4,3 g</span></div>
        <div class="row"><span>Eiweiß</span><span>0,1 g</span></div>
        <div class="row"><span>Salz</span><span>0,06 g</span></div>
        <div class="row"><span>Vitamin C</span><span>14,4 mg / 18%*</span></div>
        <div class="row"><span>Niacin</span><span>2,9 mg / 18%*</span></div>
        <div class="row"><span>Vitamin E</span><span>2,16 mg / 18%*</span></div>
        <div class="row"><span>Pantothensäure</span><span>1,08 mg / 18%*</span></div>
        <div class="row"><span>Folsäure</span><span>36,0 µg / 18%*</span></div>
        <div class="row"><span>Biotin</span><span>9,0 µg / 18%*</span></div>
        <div class="row"><span>*NRV = Referenzmenge für die tägliche Zufuhr</span></div>
      </div>
      <div class="maker">
        <b>Hersteller:</b>
        <div class="brand"><i></i><span>Hollert GmbH</span></div>
        Werkstraße 12<br>93099 Lindbach<br><b>www.canfabrik.de</b><br><br>
        <b>Vertrieb:</b><br>Musterfirma GmbH<br>Musterstraße 1<br>00000 Musterstadt
      </div>
    </div>
    <div class="icons" aria-hidden="true">
      <svg viewBox="0 0 20 20"><circle cx="10" cy="10" r="9" fill="none" stroke="#fff" stroke-width="1.6"/><path d="M6 11a4 4 0 0 1 7-3l1-2v5h-5l2-1.5A2.5 2.5 0 0 0 8 11z" fill="#fff"/></svg>
      <svg viewBox="0 0 20 20"><circle cx="10" cy="10" r="9" fill="none" stroke="#fff" stroke-width="1.6"/><text x="10" y="12.5" font-size="7" text-anchor="middle" fill="#fff" font-family="Arimo,sans-serif">alu</text></svg>
    </div>
    <div class="made">MADE IN GERMANY</div>
    <div class="volume">Inhalt<br>250ml ℮</div>
    <div class="powered"><span class="dot"></span>POWERED BY<br>BRAKELINE MOTORS</div>
    <div class="track" role="img" aria-label="Tyre track with paint splatter"></div>
    <div class="vert flavour"><span>ISO ISO ISO</span></div>
    <div class="vert sub"><span>DRINK FLAVOUR</span></div>
    <div class="vert brandmark"><span>BRAKELINE<br>MOTORS</span></div>
    <div class="vert tagline"><span>PASSION <em>●</em> PRECISION <em>●</em> PERFORMANCE</span></div>
  </section>

  <!-- MANGO -->
  <section class="label mango">
    <div class="info">
      <h2>ISO-Drink</h2>
      <p><b>Isotonisches Erfrischungsgetränk Grapefruit-Zitronen-geschmack mit Zucker und Süßungsmitteln. 6 Vitamine zugesetzt.</b></p>
      <p><b>Zutaten:</b> Wasser, Fruktosesirup, 2,5% Orangensaft aus Orangensaftkonzentrat, 2% Grapefruitsaft aus Grapefruitsaftkonzentrat, 1,5% Zitronensaft aus Zitronensaftkonzentrat, Kohlensäure, Zitronenextrakt, Säuerungsmittel, Citronensäure, Säureregulator: Kaliumcitrate, Magnesiumcarbonate; Süßungsmittel: Cyclamat, Saccharin; natürliches Citrusaroma, Vitaminmischung: Vitamin C, Niacin, Vitamin E, Pantothensäure, Folsäure, Biotin; Stabilisator: Johannisbrotkernmehl, Antioxidationsmittel: Ascorbinsäure.</p>
      <p>Mindestens haltbar bis: siehe Boden. Kühl und trocken lagern.</p>
      <div class="nutrition">
        <div class="row head"><span>Durchschnittliche Nährwerte je 100ml</span></div>
        <div class="row"><span>Brennwert</span><span>79 kJ (19 kcal)</span></div>
        <div class="row"><span>Fett</span><span>0 g</span></div>
        <div class="row"><span>- davon gesättigte Fettsäuren</span><span>0 g</span></div>
        <div class="row"><span>Kohlenhydrate</span><span>4,3 g</span></div>
        <div class="row"><span>- davon Zucker</span><span>4,3 g</span></div>
        <div class="row"><span>Eiweiß</span><span>0,1 g</span></div>
        <div class="row"><span>Salz</span><span>0,06 g</span></div>
        <div class="row"><span>Vitamin C</span><span>14,4 mg / 18%*</span></div>
        <div class="row"><span>Niacin</span><span>2,9 mg / 18%*</span></div>
        <div class="row"><span>Vitamin E</span><span>2,16 mg / 18%*</span></div>
        <div class="row"><span>Pantothensäure</span><span>1,08 mg / 18%*</span></div>
        <div class="row"><span>Folsäure</span><span>36,0 µg / 18%*</span></div>
        <div class="row"><span>Biotin</span><span>9,0 µg / 18%*</span></div>
        <div class="row"><span>*NRV = Referenzmenge für die tägliche Zufuhr</span></div>
      </div>
      <div class="maker">
        <b>Hersteller:</b>
        <div class="brand"><i></i><span>Hollert GmbH</span></div>
        Werkstraße 12<br>93099 Lindbach<br><b>www.canfabrik.de</b><br><br>
        <b>Vertrieb:</b><br>Musterfirma GmbH<br>Musterstraße 1<br>00000 Musterstadt
      </div>
    </div>
    <div class="icons" aria-hidden="true">
      <svg viewBox="0 0 20 20"><circle cx="10" cy="10" r="9" fill="none" stroke="#fff" stroke-width="1.6"/><path d="M6 11a4 4 0 0 1 7-3l1-2v5h-5l2-1.5A2.5 2.5 0 0 0 8 11z" fill="#fff"/></svg>
      <svg viewBox="0 0 20 20"><circle cx="10" cy="10" r="9" fill="none" stroke="#fff" stroke-width="1.6"/><text x="10" y="12.5" font-size="7" text-anchor="middle" fill="#fff" font-family="Arimo,sans-serif">alu</text></svg>
    </div>
    <div class="made">MADE IN GERMANY</div>
    <div class="volume">Inhalt<br>250ml ℮</div>
    <div class="powered"><span class="dot"></span>POWERED BY<br>BRAKELINE MOTORS</div>
    <div class="track" role="img" aria-label="Tyre track with paint splatter"></div>
    <div class="vert flavour"><span>Mango</span></div>
    <div class="vert sub"><span>DRINK FLAVOUR</span></div>
    <div class="vert brandmark"><span>BRAKELINE<br>MOTORS</span></div>
    <div class="vert tagline"><span>PASSION <em>●</em> PRECISION <em>●</em> PERFORMANCE</span></div>
  </section>

  <!-- ENERGY -->
  <section class="label energy">
    <div class="info">
      <h2>ENERGY DRINK</h2>
      <p><b>Koffeinhaltiges Erfrischungsgetränk mit Zusatz von 4 Vitaminen. Erhöhter Koffeingehalt (30 mg/100 ml). Für Kinder, schwangere oder stillende Frauen nicht empfohlen.</b></p>
      <p><b>Zutaten:</b> Wasser, Zucker, Dextrose, Säuerungsmittel Citronensäure, Kohlensäure, Säureregulator Natriumcitrate, Koffein, Taurin (0,03%), Farbstoffe E150c und E101, Inosit, Aroma, Niacin, Pantothensäure, Vitamin B6, Vitamin B12.</p>
      <p>Mindestens haltbar bis Ende: siehe Dosenboden.<br>Kühl und trocken lagern.</p>
      <div class="nutrition">
        <div class="row head"><span>Durchschnittliche Nährwerte je 100ml</span></div>
        <div class="row"><span>Brennwert</span><span>195 kJ(45,9 kcal)</span></div>
        <div class="row"><span>Fett</span><span>0 g</span></div>
        <div class="row"><span>- davon gesättigte Fettsäuren</span><span>0 g</span></div>
        <div class="row"><span>Kohlenhydrate</span><span>10,9 g</span></div>
        <div class="row"><span>- davon Zucker</span><span>10,9 g</span></div>
        <div class="row"><span>Eiweiß</span><span>0,06 g</span></div>
        <div class="row"><span>Salz</span><span>0,273 g</span></div>
        <div class="row gap"><span>Vitamine</span></div>
        <div class="row"><span>Niacin</span><span>7,92 mg/49,5%*</span></div>
        <div class="row"><span>Pantothensäure</span><span>1,98 mg/33,0%*</span></div>
        <div class="row"><span>Vitamin B6</span><span>2 mg/143,0%*</span></div>
        <div class="row"><span>Vitamin B12</span><span>2 µg/80,0%*</span></div>
        <div class="row"><span>*NRV = Referenzmenge für die tägliche Zufuhr</span></div>
      </div>
      <div class="maker">
        <b>Hersteller:</b>
        <div class="brand"><i></i><span>Hollert GmbH</span></div>
        Werkstraße 12<br>93099 Lindbach<br><b>www.canfabrik.de</b><br><br>
        Musterfirma GmbH<br>Musterstraße 1<br>00000 Musterstadt
      </div>
    </div>
    <div class="icons" aria-hidden="true">
      <svg viewBox="0 0 20 20"><circle cx="10" cy="10" r="9" fill="none" stroke="#fff" stroke-width="1.6"/><path d="M6 11a4 4 0 0 1 7-3l1-2v5h-5l2-1.5A2.5 2.5 0 0 0 8 11z" fill="#fff"/></svg>
      <svg viewBox="0 0 20 20"><circle cx="10" cy="10" r="9" fill="none" stroke="#fff" stroke-width="1.6"/><text x="10" y="12.5" font-size="7" text-anchor="middle" fill="#fff" font-family="Arimo,sans-serif">alu</text></svg>
    </div>
    <div class="made">MADE IN GERMANY</div>
    <div class="volume">Inhalt<br>250ml ℮</div>
    <div class="powered"><span class="dot"></span>POWERED BY<br>BRAKELINE MOTORS</div>
    <div class="track" role="img" aria-label="Tyre track with paint splatter"></div>
    <div class="vert flavour"><span>ENERGY</span></div>
    <div class="vert sub"><span>DRINK FLAVOUR</span></div>
    <div class="vert brandmark"><span>BRAKELINE<br>MOTORS</span></div>
    <div class="vert tagline"><span>PASSION <em>●</em> PRECISION <em>●</em> PERFORMANCE</span></div>
  </section>

  <!-- COLAMIX -->
  <section class="label cola">
    <div class="info">
      <h2>ENERGY DRINK</h2>
      <p><b>Koffeinhaltiges Erfrischungsgetränk mit Zusatz von 4 Vitaminen. Erhöhter Koffeingehalt (30 mg/100 ml). Für Kinder, schwangere oder stillende Frauen nicht empfohlen.</b></p>
      <p><b>Zutaten:</b> Wasser, Zucker, Dextrose, Säuerungsmittel Citronensäure, Kohlensäure, Säureregulator Natriumcitrate, Koffein, Taurin (0,03%), Farbstoffe E150c und E101, Inosit, Aroma, Niacin, Pantothensäure, Vitamin B6, Vitamin B12.</p>
      <p>Mindestens haltbar bis Ende: siehe Dosenboden.<br>Kühl und trocken lagern.</p>
      <div class="nutrition">
        <div class="row head"><span>Durchschnittliche Nährwerte je 100ml</span></div>
        <div class="row"><span>Brennwert</span><span>195 kJ(45,9 kcal)</span></div>
        <div class="row"><span>Fett</span><span>0 g</span></div>
        <div class="row"><span>- davon gesättigte Fettsäuren</span><span>0 g</span></div>
        <div class="row"><span>Kohlenhydrate</span><span>10,9 g</span></div>
        <div class="row"><span>- davon Zucker</span><span>10,9 g</span></div>
        <div class="row"><span>Eiweiß</span><span>0,06 g</span></div>
        <div class="row"><span>Salz</span><span>0,273 g</span></div>
        <div class="row gap"><span>Vitamine</span></div>
        <div class="row"><span>Niacin</span><span>7,92 mg/49,5%*</span></div>
        <div class="row"><span>Pantothensäure</span><span>1,98 mg/33,0%*</span></div>
        <div class="row"><span>Vitamin B6</span><span>2 mg/143,0%*</span></div>
        <div class="row"><span>Vitamin B12</span><span>2 µg/80,0%*</span></div>
        <div class="row"><span>*NRV = Referenzmenge für die tägliche Zufuhr</span></div>
      </div>
      <div class="maker">
        <b>Hersteller:</b>
        <div class="brand"><i></i><span>Hollert GmbH</span></div>
        Werkstraße 12<br>93099 Lindbach<br><b>www.canfabrik.de</b><br><br>
        Musterfirma GmbH<br>Musterstraße 1<br>00000 Musterstadt
      </div>
    </div>
    <div class="icons" aria-hidden="true">
      <svg viewBox="0 0 20 20"><circle cx="10" cy="10" r="9" fill="none" stroke="#fff" stroke-width="1.6"/><path d="M6 11a4 4 0 0 1 7-3l1-2v5h-5l2-1.5A2.5 2.5 0 0 0 8 11z" fill="#fff"/></svg>
      <svg viewBox="0 0 20 20"><circle cx="10" cy="10" r="9" fill="none" stroke="#fff" stroke-width="1.6"/><text x="10" y="12.5" font-size="7" text-anchor="middle" fill="#fff" font-family="Arimo,sans-serif">alu</text></svg>
    </div>
    <div class="made">MADE IN GERMANY</div>
    <div class="volume">Inhalt<br>250ml ℮</div>
    <div class="powered"><span class="dot"></span>POWERED BY<br>BRAKELINE MOTORS</div>
    <div class="track" role="img" aria-label="Tyre track with paint splatter"></div>
    <div class="vert flavour"><span>Colamix</span></div>
    <div class="vert sub"><span>DRINK FLAVOUR</span></div>
    <div class="vert brandmark"><span>BRAKELINE<br>MOTORS</span></div>
    <div class="vert tagline"><span>PASSION <em>●</em> PRECISION <em>●</em> PERFORMANCE</span></div>
  </section>

</main>
</body>
</html>
```